Event Poster for Bar Sunday Live Music and Happy Hour

We are a bar. Every Sunday we have a HARBOUR HOURS event where we have live music and a Sunday Happy Hour. I would like a poster that promotes this weekly event in A4 and A3. Information the poster should include:Event Name: SUNDAY SESSIONSVenue: Copper Lantern 218-222 Marlow Rd PrestonDrink Specials: 3:00 pm - 5:00pmLive Music: 4:30pm -6:30pmAttached is our logo.

Target Market(s)

Both sexes 30-40 year olds

Industry/Entity Type

Hospitality

Font styles to use
Sans Serif

Colors

Designer to choose colors to be used in the design.

Requirements
Must have
• Event Name: HARBOUR HOURS
• Venue: Copper Lantern 218-222 Marlow Rd Preston
• Drink Specials: 3:00 pm - 5:00pm
• Live Music: 4:30pm -6:30pm
• Logo
Nice to have
• Open to different styles and ideas. Like colour.
Should not have
• It should not be too blokey are over the top bar-like.

```html
<!DOCTYPE html>
<html lang="en">
<head>
<meta charset="utf-8">
<title>Harbour Hours – Copper Lantern</title>
<link rel="stylesheet" href="https://fonts.googleapis.com/css2?family=Poiret+One&family=Yellowtail&display=swap">
<style>
  :root {
    --sky-pink: #e9c6d6;
    --sky-rose: #d9a2a8;
    --sky-mist: #e8eef2;
    --sky-steel: #9db2c2;
    --sky-deep: #2b3f5c;
    --title-blue: #1f4c7a;
    --title-pink: #eaa0ad;
    --ink: #151515;
    --badge-black: #000;
    --badge-ring: #fff;
    --badge-text: #d9a0a6;
  }
  html, body {
    margin: 0;
    padding: 0;
    overflow: hidden;
  }
  .poster {
    position: relative;
    width: 848px;
    height: 1200px;
    overflow: hidden;
    font-family: "Poiret One", sans-serif;
    color: var(--ink);
  }
  .sky {
    position: absolute;
    inset: 0;
    background: linear-gradient(180deg,
      var(--sky-pink) 0%,
      var(--sky-rose) 30%,
      var(--sky-mist) 52%,
      var(--sky-steel) 72%,
      var(--sky-deep) 100%);
  }
  .script-title {
    position: absolute;
    left: 0;
    width: 848px;
    overflow: visible;
  }
  .script-title text {
    font-family: "Yellowtail", cursive;
  }
  .script-title--top { top: 0; height: 280px; }
  .script-title--bottom { top: 920px; height: 280px; }
  .badge {
    position: absolute;
    left: 180px;
    top: 268px;
    width: 472px;
    height: 472px;
    border-radius: 50%;
    background: var(--badge-black);
    border: 8px solid var(--badge-ring);
    display: flex;
    flex-direction: column;
    align-items: center;
    justify-content: center;
    text-align: center;
  }
  .badge__name {
    margin: 0;
    font-size: 64px;
    line-height: 1.1;
    letter-spacing: 4px;
    color: var(--badge-text);
    font-weight: 400;
  }
  .details {
    position: absolute;
    left: 0;
    top: 770px;
    width: 848px;
    text-align: center;
  }
  .details__address {
    margin: 0;
    font-size: 50px;
    letter-spacing: 1px;
  }
  .details__times {
    margin: 8px 0 0;
    font-size: 36px;
    line-height: 1.45;
  }
</style>
</head>
<body>
  <main class="poster">
    <div class="sky" role="img" aria-label="Soft sky of pink and blue clouds fading to deep blue"></div>

    <svg class="script-title script-title--top" viewBox="0 0 848 280" aria-hidden="false">
      <text x="0" y="225" font-size="230" fill="var(--title-blue)" textLength="848" lengthAdjust="spacingAndGlyphs">Harbour</text>
    </svg>

    <div class="badge">
      <p class="badge__name">COPPER<br>LANTERN</p>
    </div>

    <section class="details">
      <p class="details__address">218-222 MARLOW RD., PRESTON</p>
      <p class="details__times">LIVE MUSIC 430-630<br>DRINK SPECIALS 300-500</p>
    </section>

    <svg class="script-title script-title--bottom" viewBox="0 0 848 280">
      <text x="60" y="230" font-size="250" fill="var(--title-pink)" textLength="770" lengthAdjust="spacingAndGlyphs">Hours</text>
    </svg>
  </main>
</body>
</html>
```